Flyer for outback tour company

Trifold flyer with a page for each tour that we offer (4 different tours) as well as a front page and a contact page.

Front page: Kestrel Treks logo + an overview of the tours on offer:
- Grand Circuit of the Village and Ridgelands
- Opalvale Showcase Tour
- Twilight Ridgelands Tour
- Subsurface Gemhunt (prospecting) Tour.

Page 2-5: description of each tour with pricing/duration.

Last page (back of brochure): contact details.
Ph: 0488 217 654
E-mail: kestreltreksoz@mailbox-example.net
Online bookings: www.kestreltreksoz-example.com.au.
Tours can also be booked directly through the reception at the Harlow Ridge Desert Lodge and the Clay Nest Inn. Please include the logos for Harlow Ridge and Clay Nest on the last page.

Target Market(s)

Travellers/tourists

Industry/Entity Type

Tourism/tour company

Font styles to use
Sans Serif

Requirements
Must have
• In regards to the pictures… the picture with the tour guide shining the torch should be on the page with the Gemhunt Tour. The other pictures of the cave tunnels should only be on the premium tour/Gemhunt Tour or front/back page.

```html
<!DOCTYPE html>
<html lang="en">
<head>
<meta charset="utf-8">
<title>Kestrel Treks – Trifold Flyer</title>
<link href="https://fonts.googleapis.com/css2?family=Montserrat:wght@400;600;700;800&family=Kaushan+Script&display=swap" rel="stylesheet">
<style>
:root{
  --navy:#1f3b8f;
  --navy-deep:#142a6b;
  --orange:#e8861f;
  --orange-deep:#c96d12;
  --sky:#2ea6df;
  --sky-light:#7fcdf0;
  --white:#ffffff;
  --ink:#1d2433;
  --grey:#5b6270;
  --page:#eeeeee;
  --rust:#a4502a;
}
*{box-sizing:border-box;margin:0;padding:0}
html,body{width:1200px;height:2399px;overflow:hidden}
body{background:var(--page);font-family:'Montserrat',sans-serif;color:var(--ink);position:relative}
.spread{position:absolute;left:0;width:1200px;height:860px;display:flex;box-shadow:0 10px 30px rgba(0,0,0,.18)}
.spread--outside{top:200px}
.spread--inside{top:1340px}
.panel{position:relative;width:400px;height:860px;overflow:hidden;background:var(--white)}
.photo{position:absolute;left:0;width:100%}
.script{font-family:'Kaushan Script',cursive;font-weight:400}
.brand{display:flex;align-items:center;gap:10px;font-family:'Montserrat',sans-serif;font-weight:800;color:var(--navy);letter-spacing:.5px}
.brand__mark{width:18px;height:18px;background:var(--orange)}
.title-band{position:absolute;left:0;width:100%;background:var(--navy);color:var(--white);text-align:center;padding:16px 20px 12px}
.title-band h2{font-family:'Kaushan Script',cursive;font-weight:400;font-size:27px;line-height:1.1}
.price-tag{display:inline-block;margin-top:8px;background:var(--orange);color:var(--white);font-family:'Kaushan Script',cursive;font-size:19px;padding:3px 22px}
.body-copy{font-size:12.5px;line-height:1.5}
.duration{font-weight:700;font-size:14px;margin-bottom:6px}
.includes-label{display:inline-block;background:var(--orange);color:var(--white);font-weight:700;font-size:12.5px;padding:3px 10px;margin:12px 0 6px}
.checklist{list-style:none}
.checklist li{display:flex;gap:7px;align-items:flex-start;font-size:12.5px;line-height:1.55}
.checklist svg{flex:none;margin-top:3px}
.note{font-size:11px;color:var(--grey);margin-top:8px}

/* Outside: gemhunt panel */
.gemhunt__photo{top:0;height:330px;background:linear-gradient(160deg,#c98a5c 0%,#b4603a 45%,#6e4a36 80%,#8c8c8c 100%)}
.gemhunt__band{top:300px;transform:skewY(-6deg);transform-origin:left;padding:20px 20px 16px}
.gemhunt__band > *{transform:skewY(6deg)}
.gemhunt__body{position:absolute;top:420px;left:0;width:100%;height:440px;background:linear-gradient(180deg,var(--orange) 0%,var(--orange-deep) 100%);color:var(--white);padding:40px 34px}
/* Outside: contact panel */
.contact__photo{top:0;height:300px;background:linear-gradient(170deg,#c07a55 0%,#b2603c 50%,#7d5a47 85%,#a79f96 100%)}
.contact__sheet{position:absolute;top:250px;left:0;width:100%;height:610px;background:var(--white);border-radius:60% 40% 0 0/40px 40px 0 0;padding:44px 34px 0;text-align:center}
.contact__sheet .brand{justify-content:center;font-size:24px}
.call-box{margin:28px auto 0;border:3px solid var(--orange);padding:12px 10px 14px;width:300px}
.call-box__label{font-weight:800;font-size:28px;color:var(--navy);letter-spacing:1px}
.call-box__phone{display:flex;align-items:center;justify-content:center;gap:8px;font-weight:800;font-size:30px;color:var(--orange)}
.call-box__email{display:inline-block;background:var(--navy);color:var(--white);font-size:11px;font-weight:600;padding:4px 8px;margin-top:8px}
.book-online{margin-top:22px;font-weight:800;font-size:20px;color:var(--navy)}
.book-online__url{font-size:13.5px;color:var(--orange);font-weight:600}
.reception{font-family:'Kaushan Script',cursive;font-size:17px;line-height:1.35;color:var(--navy);margin-top:22px}
.partners{display:flex;align-items:center;justify-content:center;gap:12px;margin-top:22px;flex-wrap:wrap}
.partner-name{display:flex;align-items:center;gap:6px;font-size:11.5px;font-weight:700;color:var(--navy)}
.partner-name i{width:12px;height:12px;background:var(--orange);display:block}
.partner-badge{width:40px;height:26px;border-radius:4px}
/* Outside: cover */
.cover{background:linear-gradient(180deg,var(--navy-deep) 0%,var(--navy) 30%,var(--sky) 55%)}
.cover__tab{position:absolute;top:0;left:70px;width:300px;height:150px;background:var(--white);border-radius:0 0 70px 70px;display:flex;align-items:center;justify-content:center}
.cover__tab .brand{font-size:27px}
.cover__title{position:absolute;top:230px;left:40px;width:320px;color:var(--white);transform:rotate(-8deg)}
.cover__frame{position:absolute;inset:0;border:3px solid var(--orange);border-left:none;border-bottom:none}
.cover__title .big{font-family:'Kaushan Script',cursive;font-size:62px;line-height:1}
.cover__title .sub{font-weight:600;font-size:17px;letter-spacing:1.5px;text-transform:uppercase;margin-top:6px}
.cover__title .sub2{font-family:'Kaushan Script',cursive;font-size:27px;line-height:1.1}
.cover__photo{top:470px;height:390px;background:linear-gradient(170deg,#6fa7c7 0%,#a8623e 20%,#b0562c 55%,#6a3d22 85%,#3b2a1f 100%)}

/* Inside: grand circuit */
.grand__photo{top:0;height:350px;background:radial-gradient(ellipse at 50% 55%,#c9863d 0%,#8a5228 40%,#4c2c18 80%)}
.grand__band{top:330px}
.grand__body{position:absolute;top:470px;left:0;width:100%;padding:18px 30px}
/* Inside: showcase */
.showcase__top{position:absolute;top:0;left:0;width:100%;height:520px;background:linear-gradient(180deg,var(--sky) 0%,#3cb0e3 60%,var(--sky-light) 100%);color:var(--white);padding:28px 30px}
.showcase__heading{background:var(--orange);margin:-28px -30px 14px;padding:18px 20px 10px;text-align:center}
.showcase__heading h2{font-family:'Kaushan Script',cursive;font-weight:400;font-size:27px}
.showcase__price{font-family:'Kaushan Script',cursive;font-size:19px;text-align:center}
.showcase__family{font-family:'Kaushan Script',cursive;font-size:17px;text-align:center;margin-bottom:12px}
.showcase__top .checklist li,.showcase__top .body-copy{color:var(--white)}
.showcase__top .note{color:#e6f5fc}
.showcase__photo{top:520px;height:340px;background:linear-gradient(180deg,#a9c9dc 0%,#c9a482 35%,#8c4e2e 70%,#3a2418 100%)}
/* Inside: twilight */
.twilight__photo{top:0;height:330px;background:linear-gradient(180deg,#1d2a66 0%,#3f4d8e 35%,#c9765a 70%,#f0a64a 85%,#2a1a14 100%)}
.twilight__band{top:300px}
.twilight__body{position:absolute;top:440px;left:0;width:100%;padding:18px 30px}
.thumbs{display:flex;gap:10px;margin-top:18px}
.thumb{width:105px;height:80px;border-radius:14px}
</style>
</head>
<body>

<!-- OUTSIDE SPREAD -->
<section class="spread spread--outside" aria-label="Flyer outside">
  <article class="panel gemhunt">
    <div class="photo gemhunt__photo" role="img" aria-label="Photo of a tour truck parked before cave tunnels cut into a red rock face"></div>
    <div class="title-band gemhunt__band">
      <h2>Subsurface Gemhunt<br>(prospecting)</h2>
      <div class="price-tag">$50</div>
    </div>
    <div class="gemhunt__body body-copy">
      <p class="duration">Duration: 2 hours | 9.30am start</p>
      <p>An amazing opportunity to access an exclusive underground mine in the opal fields to try your hand at prospecting. This tour is ideal for those who want to get down and dirty while searching for their own opals. Exclusive to Kestrel Treks, this impressive mine has yielded thousands of dollars worth of opal. After a quick introduction to mining, you will be handed a blacklight, pick and shovel to explore the tunnels in the hope of finding your own piece of opal to take home with you. A truly unique experience.</p>
    </div>
  </article>

  <article class="panel contact">
    <div class="photo contact__photo" role="img" aria-label="Photo continuing the red rock cliff with cave tunnels"></div>
    <div class="contact__sheet">
      <div class="brand"><span class="brand__mark"></span>KESTREL TREKS</div>
      <div class="call-box">
        <div class="call-box__label">CALL US</div>
        <div class="call-box__phone">
          <svg width="22" height="22" viewBox="0 0 24 24" aria-hidden="true"><path fill="#e8861f" d="M6.6 10.8a15 15 0 0 0 6.6 6.6l2.2-2.2a1 1 0 0 1 1-.25 11.4 11.4 0 0 0 3.6.57 1 1 0 0 1 1 1V20a1 1 0 0 1-1 1A17 17 0 0 1 3 4a1 1 0 0 1 1-1h3.5a1 1 0 0 1 1 1c0 1.25.2 2.45.57 3.57a1 1 0 0 1-.25 1z"/></svg>
          0488 217 654
        </div>
        <div class="call-box__email">kestreltreksoz@mailbox-example.net</div>
      </div>
      <div class="book-online">BOOK ONLINE</div>
      <div class="book-online__url">www.kestreltreksoz-example.com.au</div>
      <p class="reception">Tours can also be booked directly through the reception at the Harlow Ridge Desert Lodge and the Clay Nest Inn</p>
      <div class="partners">
        <span class="partner-name"><i></i>Harlow Ridge</span>
        <span class="partner-badge" style="background:var(--sky)"></span>
        <span class="partner-badge" style="background:#9cc54a"></span>
        <span class="partner-name"><i></i>Clay Nest</span>
      </div>
    </div>
  </article>

  <article class="panel cover">
    <div class="cover__tab"><div class="brand"><span class="brand__mark"></span>KESTREL TREKS</div></div>
    <div class="cover__title">
      <div class="big">Grand Circuit</div>
      <div class="sub">of the Village</div>
      <div class="sub2">and Ridgelands</div>
    </div>
    <div class="photo cover__photo" role="img" aria-label="Photo of a red and ochre outback mesa under a blue sky"></div>
  </article>
</section>

<!-- INSIDE SPREAD -->
<section class="spread spread--inside" aria-label="Flyer inside">
  <article class="panel grand">
    <div class="photo grand__photo" role="img" aria-label="Photo of stained glass windows inside an underground church"></div>
    <div class="title-band grand__band">
      <h2>Grand Circuit of the Village<br>and the Ridgelands</h2>
      <div class="price-tag">$99 adults / $75 children</div>
    </div>
    <div class="grand__body">
      <p class="duration">Duration: 5 hours | 1.00pm start</p>
      <p class="body-copy">This tour is designed for those who want a more personal, authentic experience. Smaller groups, bigger experience. Sit back and relax in our spacious air-conditioned 4WD vehicle as we take you places in and around Opalvale that the others can't.</p>
      <span class="includes-label">THE TOUR INCLUDES:</span>
      <ul class="checklist">
        <li><svg width="11" height="11" viewBox="0 0 12 12"><rect x=".5" y=".5" width="11" height="11" fill="none" stroke="#1f3b8f"/><path d="M2.5 6l2.5 2.5 4.5-5" fill="none" stroke="#1f3b8f" stroke-width="1.6"/></svg>The Old Stone Underground Church</li>
        <li><svg width="11" height="11" viewBox="0 0 12 12"><rect x=".5" y=".5" width="11" height="11" fill="none" stroke="#1f3b8f"/><path d="M2.5 6l2.5 2.5 4.5-5" fill="none" stroke="#1f3b8f" stroke-width="1.6"/></svg>Modern Underground Home (dugout)</li>
        <li><svg width="11" height="11" viewBox="0 0 12 12"><rect x=".5" y=".5" width="11" height="11" fill="none" stroke="#1f3b8f"/><path d="M2.5 6l2.5 2.5 4.5-5" fill="none" stroke="#1f3b8f" stroke-width="1.6"/></svg>The Moon Plains</li>
        <li><svg width="11" height="11" viewBox="0 0 12 12"><rect x=".5" y=".5" width="11" height="11" fill="none" stroke="#1f3b8f"/><path d="M2.5 6l2.5 2.5 4.5-5" fill="none" stroke="#1f3b8f" stroke-width="1.6"/></svg>The Dingo Fence</li>
        <li><svg width="11" height="11" viewBox="0 0 12 12"><rect x=".5" y=".5" width="11" height="11" fill="none" stroke="#1f3b8f"/><path d="M2.5 6l2.5 2.5 4.5-5" fill="none" stroke="#1f3b8f" stroke-width="1.6"/></svg>The Ridgelands</li>
        <li><svg width="11" height="11" viewBox="0 0 12 12"><rect x=".5" y=".5" width="11" height="11" fill="none" stroke="#1f3b8f"/><path d="M2.5 6l2.5 2.5 4.5-5" fill="none" stroke="#1f3b8f" stroke-width="1.6"/></svg>Underground Mine Tour at our private claim in the opal fields (exclusive to Kestrel Treks)</li>
        <li><svg width="11" height="11" viewBox="0 0 12 12"><rect x=".5" y=".5" width="11" height="11" fill="none" stroke="#1f3b8f"/><path d="M2.5 6l2.5 2.5 4.5-5" fill="none" stroke="#1f3b8f" stroke-width="1.6"/></svg>Complimentary glass of sparkling wine will be provided for the adults at the Ridgelands lookout.</li>
      </ul>
      <p class="note">(This tour utilises a 4WD Ranger Hauler)</p>
    </div>
  </article>

  <article class="panel showcase">
    <div class="showcase__top">
      <div class="showcase__heading"><h2>Opalvale Showcase Tour</h2></div>
      <p class="showcase__price">$85 adults / $59 children</p>
      <p class="showcase__family">Family rate: $270 (2 adults and 2 children)</p>
      <p class="duration">Duration: 5 hours | 1.00pm start</p>
      <p class="body-copy">A tour that gives you a great insight and introduction into this unique outback town and the surrounding area. Highlights include:</p>
      <ul class="checklist" style="margin-top:8px">
        <li><svg width="11" height="11" viewBox="0 0 12 12"><rect x=".5" y=".5" width="11" height="11" fill="none" stroke="#fff"/><path d="M2.5 6l2.5 2.5 4.5-5" fill="none" stroke="#fff" stroke-width="1.6"/></svg>Quartzhollow Opal Mine &amp; Museum (incl. award-winning movie, underground house tour and mine tour)</li>
        <li><svg width="11" height="11" viewBox="0 0 12 12"><rect x=".5" y=".5" width="11" height="11" fill="none" stroke="#fff"/><path d="M2.5 6l2.5 2.5 4.5-5" fill="none" stroke="#fff" stroke-width="1.6"/></svg>The Old Stone Underground Church</li>
        <li><svg width="11" height="11" viewBox="0 0 12 12"><rect x=".5" y=".5" width="11" height="11" fill="none" stroke="#fff"/><path d="M2.5 6l2.5 2.5 4.5-5" fill="none" stroke="#fff" stroke-width="1.6"/></svg>The Dingo Fence</li>
        <li><svg width="11" height="11" viewBox="0 0 12 12"><rect x=".5" y=".5" width="11" height="11" fill="none" stroke="#fff"/><path d="M2.5 6l2.5 2.5 4.5-5" fill="none" stroke="#fff" stroke-width="1.6"/></svg>The Moon Plains</li>
        <li><svg width="11" height="11" viewBox="0 0 12 12"><rect x=".5" y=".5" width="11" height="11" fill="none" stroke="#fff"/><path d="M2.5 6l2.5 2.5 4.5-5" fill="none" stroke="#fff" stroke-width="1.6"/></svg>The Ridgelands</li>
      </ul>
      <p class="note">(This tour utilises a Ranger Coach)</p>
    </div>
    <div class="photo showcase__photo" role="img" aria-label="Photo of two glasses of sparkling wine on red desert ground at the lookout"></div>
  </article>

  <article class="panel twilight">
    <div class="photo twilight__photo" role="img" aria-label="Photo of a mining machine silhouetted against a sunset sky"></div>
    <div class="title-band twilight__band">
      <h2>Twilight Ridgelands Tour</h2>
      <div class="price-tag">$60</div>
    </div>
    <div class="twilight__body">
      <p class="duration">Duration: 3.5 hours | Departs 3 hours before sunset</p>
      <p class="body-copy">A perfect way to end the day. Take in the spectacular views of the colourful Ridgelands. Watch the sun go down across the desert horizon while enjoying a hot beverage (tea, coffee, hot chocolate) in one hand and a home-made scone in the other.</p>
      <span class="includes-label">THE TOUR INCLUDES:</span>
      <ul class="checklist">
        <li><svg width="11" height="11" viewBox="0 0 12 12"><rect x=".5" y=".5" width="11" height="11" fill="none" stroke="#1f3b8f"/><path d="M2.5 6l2.5 2.5 4.5-5" fill="none" stroke="#1f3b8f" stroke-width="1.6"/></svg>The Dingo Fence</li>
        <li><svg width="11" height="11" viewBox="0 0 12 12"><rect x=".5" y=".5" width="11" height="11" fill="none" stroke="#1f3b8f"/><path d="M2.5 6l2.5 2.5 4.5-5" fill="none" stroke="#1f3b8f" stroke-width="1.6"/></svg>The Moon Plains</li>
        <li><svg width="11" height="11" viewBox="0 0 12 12"><rect x=".5" y=".5" width="11" height="11" fill="none" stroke="#1f3b8f"/><path d="M2.5 6l2.5 2.5 4.5-5" fill="none" stroke="#1f3b8f" stroke-width="1.6"/></svg>The Ridgelands</li>
      </ul>
      <div class="thumbs">
        <div class="thumb" style="background:linear-gradient(180deg,#5d8fd0,#c77a48)" role="img" aria-label="Photo of desert plains under blue sky"></div>
        <div class="thumb" style="background:radial-gradient(circle,#8a8a6a,#2c2a22)" role="img" aria-label="Photo of a dim underground tunnel"></div>
        <div class="thumb" style="background:linear-gradient(180deg,#9ab7cf,#a25a34)" role="img" aria-label="Photo of a cave opening looking out to the desert"></div>
      </div>
    </div>
  </article>
</section>

</body>
</html>
```